Varno Building Pty Ltd need an Identity!

We need a logo design for a building company based in Sydney, Australia. In addition - Business Card Layout. The colour scheme is to be black and red and communicate a professional yet 'hands on' approach to building.

Target Market(s)

Architects, Home Owners, Developers

Industry/Entity Type

Construction

Font styles to use
Serif
Sans Serif

Colors
ec1f27

Requirements
Must have
• Clear logo and professional direction.
Nice to have
• Use of initials as a possible logo
Should not have
• Graphics/pictures of houses, house roofs etc. Can be an abstracted form of a building.

```html
<!DOCTYPE html>
<html lang="en">
<head>
<meta charset="utf-8">
<title>Varno Building Pty Ltd – Letterhead and Business Card</title>
<link href="https://fonts.googleapis.com/css2?family=Saira:wght@600&family=Arimo:wght@700&display=swap" rel="stylesheet">
<style>
  :root {
    --red: #ec1f27;
    --bright-red: #ff0000;
    --black: #000000;
    --white: #ffffff;
    --edge: #d6d6d6;
    --shade: #3a3a3a;
  }
  html, body {
    margin: 0;
    padding: 0;
    width: 1200px;
    height: 1200px;
    overflow: hidden;
    background: var(--white);
  }
  .canvas {
    position: relative;
    width: 1200px;
    height: 1200px;
  }

  /* Letterhead */
  .letterhead {
    position: absolute;
    left: 48px;
    top: 40px;
    width: 790px;
    height: 1120px;
    border: 1px solid var(--edge);
    box-sizing: border-box;
    overflow: hidden;
  }
  .letterhead-frame {
    position: absolute;
    left: 86px;
    top: 99px;
    width: 661px;
    height: 108px;
    border: 3px solid var(--bright-red);
    box-sizing: border-box;
  }
  .letterhead-mark {
    position: absolute;
    left: 48px;
    top: 62px;
    width: 84px;
    height: 84px;
    background: var(--red);
  }
  .company-name {
    font-family: "Saira", "Arial", sans-serif;
    font-weight: 600;
    color: var(--black);
    white-space: nowrap;
    margin: 0;
  }
  .letterhead .company-name {
    position: absolute;
    left: 222px;
    top: 100px;
    font-size: 48px;
    line-height: 1;
    letter-spacing: 0.5px;
  }
  .contact {
    font-family: "Arimo", "Arial", sans-serif;
    font-weight: 700;
    color: var(--bright-red);
    white-space: nowrap;
    margin: 0;
  }
  .letterhead .contact {
    position: absolute;
    left: 226px;
    top: 162px;
    font-size: 16px;
    line-height: 19px;
  }
  .letterhead-band {
    position: absolute;
    left: 0;
    bottom: 0;
    width: 100%;
    height: 110px;
  }

  /* Business card */
  .business-card {
    position: absolute;
    left: 871px;
    top: 362px;
    width: 279px;
    height: 475px;
    border: 1px solid var(--edge);
    box-sizing: border-box;
    overflow: hidden;
  }
  .card-frame {
    position: absolute;
    left: 38px;
    top: 25px;
    width: 66px;
    height: 397px;
    border: 2px solid var(--bright-red);
    box-sizing: border-box;
  }
  .card-mark {
    position: absolute;
    left: 12px;
    top: 352px;
    width: 62px;
    height: 62px;
    background: var(--red);
  }
  .card-identity {
    position: absolute;
    left: 44px;
    top: 30px;
    height: 312px;
    writing-mode: vertical-rl;
    transform: rotate(180deg);
    text-align: start;
  }
  .business-card .company-name {
    font-size: 30px;
    line-height: 34px;
  }
  .business-card .contact {
    font-size: 9.6px;
    line-height: 11px;
  }
  .card-person {
    position: absolute;
    left: 148px;
    top: 150px;
    height: 180px;
    writing-mode: vertical-rl;
    transform: rotate(180deg);
    text-align: center;
    font-family: "Arimo", "Arial", sans-serif;
    font-weight: 700;
    color: var(--bright-red);
  }
  .person-name {
    font-size: 11px;
    line-height: 13px;
  }
  .person-role {
    font-size: 5.5px;
    line-height: 8px;
  }
  .card-band {
    position: absolute;
    right: 0;
    top: 0;
    width: 68px;
    height: 100%;
  }
</style>
</head>
<body>
<div class="canvas">

  <section class="letterhead">
    <div class="letterhead-frame"></div>
    <div class="letterhead-mark"></div>
    <h1 class="company-name">Varno Building Pty Ltd</h1>
    <p class="contact">Address : xoxoxoxo, xoxo xoxoxo, xoxoxo - xoxoxo<br>Cell : 90909090 E-mail : varnobuilding@mail.com</p>
    <svg class="letterhead-band" role="img" aria-label="Decorative band of red and black building blocks" viewBox="0 0 790 110" preserveAspectRatio="none">
      <defs>
        <linearGradient id="bandFill" x1="0" y1="0" x2="1" y2="0">
          <stop offset="0" stop-color="#3a3a3a"/>
          <stop offset="0.25" stop-color="#ec1f27"/>
          <stop offset="0.5" stop-color="#3a3a3a"/>
          <stop offset="0.75" stop-color="#ec1f27"/>
          <stop offset="1" stop-color="#3a3a3a"/>
        </linearGradient>
      </defs>
      <rect x="0" y="0" width="790" height="110" fill="url(#bandFill)"/>
    </svg>
  </section>

  <section class="business-card">
    <div class="card-frame"></div>
    <div class="card-mark"></div>
    <div class="card-identity">
      <h2 class="company-name">Varno Building Pty Ltd</h2>
      <p class="contact">Address : xoxoxoxo, xoxo xoxoxo, xoxoxo - xoxoxo<br>Cell : 90909090 E-mail : varnobuilding@mail.com</p>
    </div>
    <div class="card-person">
      <div class="person-name">Your Name</div>
      <div class="person-role">Designation</div>
    </div>
    <svg class="card-band" role="img" aria-label="Decorative column of red and black building blocks" viewBox="0 0 68 475" preserveAspectRatio="none">
      <defs>
        <linearGradient id="cardBandFill" x1="0" y1="0" x2="0" y2="1">
          <stop offset="0" stop-color="#3a3a3a"/>
          <stop offset="0.33" stop-color="#ec1f27"/>
          <stop offset="0.66" stop-color="#3a3a3a"/>
          <stop offset="1" stop-color="#ec1f27"/>
        </linearGradient>
      </defs>
      <rect x="0" y="0" width="68" height="475" fill="url(#cardBandFill)"/>
    </svg>
  </section>

</div>
</body>
</html>
```